Brell Harbor Company Business Cards

Front and Back Business Card - logo and text setup - cool design. I need workable photoshop or illustrator files so I can setup each employee card with design that is created
Updates

Hi everyone, thank you for the great entries. Please no more white and blue cards - there are so many already - black and silver only now please. thanks!

Target Market(s)

Construction Industry - Facility Managers

Industry/Entity Type

Construction

Contact Information for Business Card

I really like contemporary simplistic looks - clean neat....not opposed to seeing some black backrounds

Requirements
Must have
• Logo/website address with design on front only - www.brellharbor-example.com (logo attached)
• Back:
• Name/Title/Company Address/Phone/email address
Nice to have
• Cool design
Should not have
• Nothing gimmicky like Fire or Water - since we are a Fire Protection company - it has all been done

```html
<!DOCTYPE html>
<html lang="en">
<head>
<meta charset="utf-8">
<title>Brell Harbor Company – Business Cards</title>
<link href="https://fonts.googleapis.com/css2?family=Lato:wght@400;700;900&display=swap" rel="stylesheet">
<style>
  :root {
    --backdrop: #c9c9c9;
    --card: #222223;
    --orange: #f04e37;
    --blue: #2d4b8e;
    --white: #f2f2f2;
  }
  html, body {
    margin: 0;
    width: 1200px;
    height: 1200px;
    overflow: hidden;
    background: var(--backdrop);
    font-family: "Lato", sans-serif;
  }
  .card {
    position: absolute;
    left: 250px;
    width: 708px;
    height: 404px;
    background: var(--card);
    box-shadow: 0 6px 14px rgba(0,0,0,0.35);
  }
  .card--front { top: 144px; }
  .card--back { top: 582px; }

  .wordmark {
    position: absolute;
    margin: 0;
    font-weight: 900;
    color: var(--orange);
    white-space: nowrap;
    letter-spacing: -0.5px;
  }
  .card--front .wordmark {
    left: 0; right: 0;
    top: 170px;
    text-align: center;
    font-size: 46px;
  }
  .front-url {
    position: absolute;
    left: 0; right: 0;
    top: 344px;
    text-align: center;
    color: var(--orange);
    font-size: 21px;
  }

  .card--back .wordmark {
    left: 52px;
    top: 182px;
    font-size: 27px;
  }
  .divider {
    position: absolute;
    left: 381px;
    top: 109px;
    width: 1.5px;
    height: 187px;
    background: var(--orange);
  }
  .details {
    position: absolute;
    left: 408px;
    top: 104px;
    color: var(--white);
    font-size: 16.5px;
    line-height: 1.25;
  }
  .person-name {
    margin: 0;
    font-size: 21px;
    font-weight: 400;
  }
  .person-name .first { color: var(--blue); }
  .person-name .last { color: var(--orange); }
  .person-title { margin: 2px 0 0; }
  .address { margin: 14px 0 0; font-style: normal; }
  .contacts { list-style: none; padding: 0; margin: 10px 0 0; }
  .contacts li {
    display: flex;
    align-items: center;
    gap: 10px;
    height: 21px;
  }
  .contacts svg { width: 14px; height: 14px; flex: none; fill: var(--orange); }
  .accent { color: var(--orange); }
</style>
</head>
<body>
  <section class="card card--front">
    <p class="wordmark">Brell Harbor Company</p>
    <p class="front-url" style="margin:0">www.brellharbor-example.com</p>
  </section>

  <section class="card card--back">
    <p class="wordmark">Brell Harbor Company</p>
    <div class="divider"></div>
    <div class="details">
      <h1 class="person-name"><span class="first">Dana</span> <span class="last">Merrow</span></h1>
      <p class="person-title">Director</p>
      <address class="address">48 Meridian Lane<br>Port Alden, NY 11000</address>
      <ul class="contacts">
        <li>
          <svg viewBox="0 0 16 16" aria-hidden="true"><path d="M3.5 1l2.5 3-1.5 1.8c.9 2 2.3 3.4 4.2 4.3L10.5 8.6l3 2.5-1.3 2.6c-.3.5-.9.7-1.5.5C6.2 12.8 3.2 9.8 1.8 5.3c-.2-.6 0-1.2.5-1.5z"/></svg>
          <span>(555) 014-2270</span>
        </li>
        <li>
          <svg viewBox="0 0 16 16" aria-hidden="true"><rect x="4" y="1" width="8" height="4"/><rect x="1" y="6" width="14" height="6" rx="1"/><rect x="4" y="10" width="8" height="5" fill="#222223"/><rect x="5" y="11" width="6" height="3"/></svg>
          <span>(555) 014-2271</span>
        </li>
        <li>
          <svg viewBox="0 0 16 16" aria-hidden="true"><path d="M1 3h14v10H1z"/><path d="M1 3l7 6 7-6" fill="none" stroke="#222223" stroke-width="1.4"/></svg>
          <span>info@brellharbor-example.com</span>
        </li>
        <li>
          <svg viewBox="0 0 16 16" aria-hidden="true"><circle cx="8" cy="8" r="6.5" fill="none" stroke="#f04e37" stroke-width="1.3"/><ellipse cx="8" cy="8" rx="2.8" ry="6.5" fill="none" stroke="#f04e37" stroke-width="1.1"/><path d="M1.5 8h13M2.5 5h11M2.5 11h11" stroke="#f04e37" stroke-width="1"/></svg>
          <span>www.<span class="accent">brellharbor-example</span>.com</span>
        </li>
      </ul>
    </div>
  </section>
</body>
</html>
```